Business Card Design Project 4 Construction Business

I am after a creative, but sleek and simple/ clean business card design. This design will form the basis of future items and might include a logo or simply a creative way to lay out the text of my company name 'kestrel ventures'
I like the simplicity of black and white however I would also be happy to see a splash of colour introduced somehow to give the text some interest and make it stand out.
I would like a double sided card.
I am young (ish!) and professional, offering construction and project management services, what I don't want is the traditional builders type card featuring a cheesy hammer/ saw image etc.
As the company name, kestrel ventures, suggests, we focus on working closely and collaboratively together, in synergy with all stakeholders involved in the projects that we undertake
Construction

```html
<!DOCTYPE html>
<html lang="en">
<head>
<meta charset="utf-8">
<title>Kestrel Ventures — Business Card</title>
<link rel="stylesheet" href="https://fonts.googleapis.com/css2?family=Josefin+Sans:wght@300;400;600&family=Oswald:wght@400;500&display=swap">
<style>
  :root {
    --backdrop-light: #d9d9d9;
    --backdrop-dark: #8a8a8a;
    --card-black: #111214;
    --gold-light: #ffd84a;
    --gold-mid: #e2b410;
    --gold-deep: #8a6208;
    --gold-text: #f2c318;
    --white: #ffffff;
    --rule-gold: #7a5a14;
  }
  * { box-sizing: border-box; margin: 0; padding: 0; }
  html, body { width: 1200px; height: 900px; overflow: hidden; }
  body {
    position: relative;
    background: radial-gradient(ellipse at 50% 35%, var(--backdrop-light) 0%, #b9b9b9 45%, var(--backdrop-dark) 100%);
    font-family: "Josefin Sans", sans-serif;
  }

  .card {
    position: absolute;
    width: 480px;
    height: 270px;
    box-shadow: 0 10px 24px rgba(0,0,0,0.35);
    overflow: hidden;
  }

  /* Front side */
  .card--front {
    left: 380px;
    top: 150px;
    background: linear-gradient(160deg, var(--gold-deep) 0%, var(--gold-mid) 30%, var(--gold-light) 55%, var(--gold-mid) 78%, var(--gold-deep) 100%);
  }
  .front-panel {
    position: absolute;
    left: 38px; right: 38px;
    top: 62px; bottom: 62px;
    background: var(--card-black);
    display: flex;
    align-items: center;
    justify-content: center;
  }
  .front-panel::before {
    content: "";
    position: absolute;
    inset: 7px;
    border: 1px solid var(--rule-gold);
  }
  .wordmark {
    font-family: "Josefin Sans", sans-serif;
    font-weight: 400;
    color: var(--white);
    letter-spacing: 0.02em;
    line-height: 1;
    white-space: nowrap;
  }
  .front-panel .wordmark { font-size: 38px; }

  /* Back side */
  .card--back {
    left: 500px;
    top: 490px;
    background: var(--card-black);
  }
  .back-gold-panel {
    position: absolute;
    left: 0; top: 0; bottom: 0;
    width: 190px;
    background: linear-gradient(170deg, var(--gold-light) 0%, var(--gold-mid) 45%, var(--gold-deep) 100%);
  }
  .back-gold-panel .wordmark {
    position: absolute;
    left: 14px;
    top: 16px;
    font-size: 27px;
  }
  .holder {
    position: absolute;
    right: 16px;
    top: 30px;
    text-align: right;
  }
  .holder-name {
    font-family: "Josefin Sans", sans-serif;
    font-weight: 300;
    font-size: 21px;
    color: var(--gold-text);
  }
  .holder-title {
    font-family: "Oswald", sans-serif;
    font-weight: 500;
    font-size: 12px;
    letter-spacing: 0.08em;
    color: var(--white);
    margin-top: 2px;
  }
  .contact {
    position: absolute;
    right: 16px;
    bottom: 16px;
    list-style: none;
    text-align: right;
    font-family: "Oswald", sans-serif;
    font-weight: 400;
    font-size: 10.5px;
    letter-spacing: 0.08em;
    line-height: 1.55;
    color: var(--white);
    text-transform: uppercase;
  }

  /* Presentation wordmark */
  .corner-wordmark {
    position: absolute;
    left: 36px;
    bottom: 40px;
    font-size: 46px;
  }
</style>
</head>
<body>

  <section class="card card--front" aria-label="Card front">
    <div class="front-panel">
      <span class="wordmark">kestrel ventures</span>
    </div>
  </section>

  <section class="card card--back" aria-label="Card back">
    <div class="back-gold-panel">
      <span class="wordmark">kestrel ventures</span>
    </div>
    <div class="holder">
      <p class="holder-name">Liam Hartwell</p>
      <p class="holder-title">DIRECTOR</p>
    </div>
    <ul class="contact">
      <li>Ph. 0400 555 018</li>
      <li>www.kestrelventuresgroup.com.au</li>
      <li>liam@kestrelventuresgroup.com.au</li>
      <li>14 Calder St Northbridge NSW 2063</li>
    </ul>
  </section>

  <span class="wordmark corner-wordmark">kestrel ventures</span>

</body>
</html>
```